Letterhead Design Project

Initially, we would like to review our letterheads.

Something simple which uses our corporate imagery well and is nicely balanced.

Please note that I will be following up this letter-head with some customised quote templates and similarly customisable collateral in the next few weeks.

Target Market(s)

Enterprise business

Industry/Entity Type

Quote

Requirements
Must have
• The Nexora9 logo
See www.nexora9.com.au

Our tagline "Enterprise Hosting, Messaging and Server Virtualisation"

Our website address

Ideally in our colour pallette, but will consider submissions which look fantastic and necessitate other colours.

```html
<!DOCTYPE html>
<html lang="en">
<head>
<meta charset="utf-8">
<title>Nexora9 Letterhead</title>
<link href="https://fonts.googleapis.com/css2?family=Questrial&display=swap" rel="stylesheet">
<style>
  :root {
    --brand-red: #d40000;
    --ink: #111111;
    --paper: #ffffff;
  }
  html, body {
    margin: 0;
    padding: 0;
    overflow: hidden;
  }
  body {
    width: 848px;
    height: 1200px;
    background: var(--paper);
    font-family: "Questrial", sans-serif;
  }
  .letterhead {
    position: relative;
    width: 848px;
    height: 1200px;
    background: var(--paper);
    overflow: hidden;
  }
  .header-brand {
    position: absolute;
    top: 48px;
    right: 58px;
    display: flex;
    align-items: center;
    gap: 8px;
  }
  .brand-square {
    width: 31px;
    height: 31px;
    background: var(--brand-red);
  }
  .brand-name {
    font-size: 36px;
    line-height: 1;
    letter-spacing: -0.5px;
    color: var(--ink);
  }
  .footer-band {
    position: absolute;
    left: 0;
    bottom: 0;
    width: 848px;
    height: 124px;
    background: var(--brand-red);
  }
  .footer-brand {
    position: absolute;
    left: 131px;
    top: 47px;
    display: flex;
    align-items: center;
    gap: 8px;
  }
  .footer-brand .brand-square {
    width: 30px;
    height: 30px;
    background: var(--paper);
  }
  .footer-brand .brand-name {
    color: var(--paper);
    font-size: 30px;
  }
  .footer-details {
    position: absolute;
    left: 293px;
    top: 48px;
    width: 420px;
    color: var(--paper);
    font-size: 13px;
    letter-spacing: 1.4px;
    line-height: 17px;
  }
  .tagline {
    margin: 0;
    white-space: nowrap;
  }
  .contact-line {
    display: flex;
    justify-content: space-between;
    margin: 0;
  }
</style>
</head>
<body>
  <div class="letterhead">
    <header class="header-brand">
      <div class="brand-square"></div>
      <span class="brand-name">Nexora9</span>
    </header>

    <footer class="footer-band">
      <div class="footer-brand">
        <div class="brand-square"></div>
        <span class="brand-name">Nexora9</span>
      </div>
      <div class="footer-details">
        <p class="tagline">Enterprise Hosting, Messaging and Server Virtualization</p>
        <p class="contact-line">
          <span class="website">www.nexora9.com.au</span>
          <span class="email">info@nexora9.com.au</span>
        </p>
      </div>
    </footer>
  </div>
</body>
</html>
```